Invitation Design for KORALT BLOSSAN Investigator Event (Exclusive Cocktail Reception)

Project Overview:
Koralt Biologics is hosting an exclusive, invitation-only cocktail reception for BLOSSAN clinical study investigators during the PWEC 2026 Conference. We need a polished, high-end event invitation designed for both email and print formats.
Event Details:
Event Name: Gather & Thrive: The BLOSSAN Investigator Event
Date: Saturday, January 24
Time: 5:00–7:00 PM
Location: Ormond Falke Steakhouse (Tarrow Private Room), Delmora Terrace
Purpose: A relaxed, come-and-go cocktail reception for BLOSSAN investigators to mingle; light content and conversation, no formal presentations.
Design Requirements:
Two logos required:
KORALT (primary)
BLOSSAN (secondary)
Color Palette: Use the Koralt color scheme, BLOSSAN color scheme, or a clean blend of both.
Tone & Style: Premium, modern, medical-professional with a high-end reception feel
Deliverable Layout:
Event title
Date & time
Location
Blurb: You are invited to a gathering for BLOSSAN clinical investigators. This event is intended to provide an opportunity for professional discussion, study related updates, and peer connection within the investigator community.
Both required logos
Clean, elegant spacing with strong hierarchy
What We Want
A visually striking but clean design that feels:
Sophisticated and corporate-professional
Consistent with our brand aesthetic
Appropriate for a high-profile physician audience
Think: elevated, clinical, modern — not flashy or overly busy.
Audience
Physicians and researchers participating in the BLOSSAN clinical study — a high-end, professional group.
Look and feel

```html
<!DOCTYPE html>
<html lang="en">
<head>
<meta charset="utf-8">
<title>Gather &amp; Thrive: The BLOSSAN Investigator Event</title>
<link href="https://fonts.googleapis.com/css2?family=Bebas+Neue&family=Montserrat:wght@200;400;500;600;700&display=swap" rel="stylesheet">
<style>
  :root {
    --page: #e9e9e9;
    --navy-deep: #0a0f4a;
    --navy: #061a6e;
    --blue: #0a2aa0;
    --teal: #03606a;
    --green: #0a9a45;
    --green-bright: #3fae3f;
    --band-green: #6cb644;
    --white: #ffffff;
    --brand-green: #6cb644;
    --brand-navy: #1b1d52;
    --brand-magenta: #c2338f;
  }
  * { margin: 0; padding: 0; box-sizing: border-box; }
  html, body {
    width: 1200px; height: 1200px; overflow: hidden;
    background: var(--page);
  }
  .invitation {
    position: absolute;
    left: 228px; top: 85px;
    width: 745px; height: 1030px;
    overflow: hidden;
    color: var(--white);
    font-family: "Montserrat", sans-serif;
    background:
      radial-gradient(ellipse 60% 35% at 55% 10%, rgba(30, 70, 220, 0.55), transparent 70%),
      radial-gradient(ellipse 50% 45% at 80% 45%, rgba(0, 140, 170, 0.45), transparent 70%),
      radial-gradient(ellipse 70% 50% at 100% 100%, rgba(40, 180, 60, 0.9), transparent 70%),
      linear-gradient(160deg, var(--blue) 0%, var(--navy-deep) 30%, var(--navy) 48%, var(--teal) 72%, var(--green) 100%);
  }
  .invitation::after {
    content: "";
    position: absolute; inset: 0;
    background: linear-gradient(20deg, rgba(20, 8, 70, 0.75) 0%, transparent 35%);
    pointer-events: none;
  }
  .title-art { position: absolute; left: 0; top: 0; width: 745px; height: 300px; }
  .title-main { font-family: "Bebas Neue", sans-serif; font-size: 212px; fill: var(--white); }
  .title-sub { font-family: "Montserrat", sans-serif; font-weight: 200; font-size: 97px; fill: var(--white); }

  .event-band {
    position: absolute; left: 6px; right: 0; top: 335px; height: 50px;
    background: linear-gradient(90deg, rgba(60,110,140,0.15) 0%, rgba(60,120,60,0.7) 25%, var(--band-green) 50%, rgba(60,120,60,0.7) 75%, rgba(60,110,140,0.15) 100%);
    border-top: 1px solid rgba(200, 240, 180, 0.5);
    display: flex; align-items: center; justify-content: center;
  }
  .event-name { font-weight: 700; font-size: 35px; letter-spacing: 0.6px; z-index: 1; }

  .details { position: absolute; left: 0; right: 0; top: 452px; text-align: center; z-index: 1; }
  .date-time { font-weight: 600; font-size: 23px; display: flex; justify-content: center; align-items: center; gap: 28px; }
  .date-time .divider { width: 3px; height: 32px; background: var(--white); }
  .venue { margin-top: 18px; font-size: 22px; line-height: 39px; }

  .blurb {
    position: absolute; left: 40px; right: 40px; top: 620px;
    text-align: center; font-size: 22.5px; line-height: 35.5px; z-index: 1;
  }

  .brand { position: absolute; z-index: 1; display: flex; align-items: center; gap: 10px; }
  .brand-primary { left: 40px; top: 918px; }
  .brand-primary .brand-name { font-weight: 500; font-size: 40px; color: var(--brand-green); letter-spacing: 1px; }
  .brand-secondary { left: 420px; top: 922px; }
  .brand-secondary .brand-mark { width: 26px; height: 26px; background: var(--brand-magenta); }
  .brand-secondary .brand-name { font-weight: 700; font-size: 40px; color: var(--brand-navy); letter-spacing: 0.5px; }
</style>
</head>
<body>
  <main class="invitation">
    <svg class="title-art" viewBox="0 0 745 300" aria-label="Gather and Thrive">
      <text class="title-main" x="115" y="188" textLength="512" lengthAdjust="spacingAndGlyphs">GATHER</text>
      <text class="title-sub" x="115" y="286" textLength="516" lengthAdjust="spacingAndGlyphs">&amp; THRIVE:</text>
    </svg>

    <div class="event-band">
      <h1 class="event-name">The BLOSSAN Investigator Event</h1>
    </div>

    <section class="details">
      <p class="date-time"><span>Saturday, January 24</span><span class="divider"></span><span>5:00–7:00 PM</span></p>
      <p class="venue">Ormond Falke Steakhouse (Tarrow Private Room),<br>Delmora Terrace</p>
    </section>

    <p class="blurb">You are invited to a gathering for BLOSSAN clinical investigators. This event is intended to provide an opportunity for professional discussion,<br>study related updates, and peer connection within the investigator community.</p>

    <div class="brand brand-primary">
      <span class="brand-name">Koralt Biologics</span>
    </div>
    <div class="brand brand-secondary">
      <span class="brand-mark"></span>
      <span class="brand-name">BLOSSAN U.S.</span>
    </div>
  </main>
</body>
</html>
```